Escrow Accounting firm needs a website design for a startup that services clients nationally.

I offer escrow accounting services for title companies and real estate attorneys. I've enclosed a logo, color palette and flyers with content that can be used for the site.

I'm looking for a similar design concept as the website below from my former employer. Please don't copy because of copyright infringement. Including for design ideas only.
www.harborlinefiduciary.com

Below is a brief write-up...
For professionals in the title insurance industry, finding a trustworthy and budget-friendly solution for escrow accounting can be daunting. When choosing the right accounting partner, title companies and law firms need a group they can rely on, and that's where we come in.

```html
<!DOCTYPE html>
<html lang="en">
<head>
<meta charset="utf-8">
<title>Meridian Escrow Partners – Escrow Accounting Services</title>
<link href="https://fonts.googleapis.com/css2?family=Poppins:wght@400;600;700;800&family=Roboto:ital,wght@0,400;0,500;0,700;1,400&display=swap" rel="stylesheet">
<style>
:root{
  --navy:#3b4556;
  --navy-dark:#2f3846;
  --copper:#b8735f;
  --copper-band:#bb7865;
  --text:#555b66;
  --light:#eef0f3;
  --white:#ffffff;
}
*{box-sizing:border-box;margin:0;padding:0}
html,body{width:1200px;height:3807px;overflow:hidden}
body{font-family:'Roboto',sans-serif;color:var(--text);background:var(--white);position:relative}
section,header,footer{position:absolute;left:0;width:1200px}
.abs{position:absolute}
.btn{display:inline-flex;align-items:center;justify-content:center;border-radius:30px;font:700 13px 'Roboto',sans-serif;text-transform:uppercase;letter-spacing:.2px;color:var(--white);background:var(--copper)}
.btn .dot{display:inline-block;width:11px;height:11px;border-radius:50%;background:currentColor;margin-left:5px;position:relative}
.sec-title{font:700 40px 'Poppins',sans-serif;color:var(--navy);text-align:center;text-transform:uppercase;letter-spacing:-.5px}
.sec-title span{color:var(--copper);font-weight:400}
.rule{width:48px;height:2px;background:var(--copper);margin:12px auto 0}

/* hero */
.hero{top:0;height:634px;background:linear-gradient(120deg,#6d6760 0%,#a79d93 35%,#cfc7bd 60%,#8f8a84 100%)}
.topbar{top:0;height:34px;background:rgba(47,56,70,.85);font:500 14px 'Roboto',sans-serif;color:var(--white)}
.topbar .item{position:absolute;top:9px;display:flex;align-items:center;gap:10px}
.topbar .ic{width:11px;height:11px;border-radius:50%;background:var(--copper)}
.social{position:absolute;right:102px;top:11px;display:flex;gap:22px}
.social i{width:11px;height:11px;border-radius:50%;background:var(--copper);display:block}
.brand{position:absolute;left:111px;top:46px;display:flex;align-items:center;gap:10px;color:var(--white);font:500 28px 'Poppins',sans-serif;letter-spacing:1px}
.brand .sq{width:28px;height:28px;border:3px solid var(--white)}
.brand small{display:block;font-size:10px;letter-spacing:2px;font-weight:400;margin-top:-8px}
.nav{position:absolute;left:511px;top:62px;display:flex;gap:32px;font:700 13px 'Roboto',sans-serif;color:var(--white);text-transform:uppercase}
.nav .active{position:relative}
.nav .active:before{content:"";position:absolute;left:0;right:0;top:-28px;height:3px;background:var(--white)}
.quote{position:absolute;left:946px;top:52px;width:142px;height:39px}
.hero h1{position:absolute;left:111px;top:212px;font:800 53px/60px 'Poppins',sans-serif;color:var(--white);text-transform:uppercase}
.get-started{position:absolute;left:111px;top:409px;width:142px;height:36px}
.arrows{position:absolute;top:546px;left:550px;display:flex;gap:12px}
.arrows span{width:44px;height:44px;border-radius:50%;background:var(--white);display:flex;align-items:center;justify-content:center}

/* about */
.about{top:634px;height:408px;background:var(--white)}
.about-photo{position:absolute;left:601px;top:0;width:599px;height:408px;background:linear-gradient(135deg,#d9d4cc,#a8a39c 55%,#5e5f66)}
.about-box{position:absolute;left:0;top:0;width:661px;height:341px;background:var(--white)}
.about h2{position:absolute;left:179px;top:80px;font:700 40px 'Poppins',sans-serif;color:var(--navy)}
.about h2 span{color:var(--copper);font-weight:400}
.about .rule{position:absolute;left:179px;top:138px;margin:0}
.about p{position:absolute;left:179px;top:158px;width:465px;font:400 15.5px/26px 'Roboto',sans-serif;text-align:justify}
.learn{position:absolute;left:179px;top:283px;width:160px;height:40px}
.dots{position:absolute;background-image:radial-gradient(#3b4556 1.2px,transparent 1.3px);background-size:7px 7px}

/* band */
.band{top:1042px;height:300px;background:var(--copper-band);text-align:center;color:var(--white)}
.band h3{margin-top:72px;font:700 27px 'Roboto',sans-serif;text-transform:uppercase}
.band h4{margin-top:4px;font:400 27px 'Roboto',sans-serif;text-transform:uppercase}
.band .btns{display:flex;justify-content:center;gap:14px;margin-top:20px}
.band .btns .btn{height:40px;padding:0 22px}
.btn.dark{background:var(--navy)}
.btn.light{background:var(--white);color:var(--navy)}

/* services */
.services{top:1342px;height:819px}
.services .sec-title{margin-top:80px}
.card{position:absolute;width:466px;height:251px;background:var(--navy);border:5px solid var(--copper);color:var(--white);font:400 15.5px/26px 'Roboto',sans-serif;padding:98px 40px 0 62px}
.card.tl{left:111px;top:173px;border-radius:0 140px 0 60px}
.card.tr{left:622px;top:173px;border-radius:140px 0 60px 0;text-align:justify;padding:98px 42px 0 62px;text-align-last:right}
.card.bl{left:111px;top:461px;border-radius:60px 0 140px 0;padding-top:92px}
.card.br{left:622px;top:461px;border-radius:0 60px 0 140px;text-align:justify;padding:92px 42px 0 62px;text-align-last:right}
.card svg{position:absolute;left:62px;top:22px}
.hub{position:absolute;left:524px;top:356px;width:152px;height:152px;border-radius:50%;background:var(--white);display:flex;align-items:center;justify-content:center}
.hub i{width:112px;height:112px;border-radius:50%;border:8px solid var(--navy);display:block}

/* testimonials */
.clients{top:2161px;height:618px;background:linear-gradient(160deg,#f3f4f6,#e6e9ee)}
.clients .sec-title{margin-top:92px}
.t-card{position:absolute;top:189px;width:306px;height:311px;background:var(--white);text-align:center;padding:26px 34px 0}
.t-card.feat{border:3px solid var(--copper)}
.stars{color:var(--copper);font-size:15px;letter-spacing:2px}
.t-card q{display:block;margin-top:10px;font:italic 400 14px/26px 'Roboto',sans-serif}
.t-card hr{border:0;border-top:1px solid #ddd;margin:14px 0 12px}
.t-card b{display:block;font:500 22px 'Roboto',sans-serif;color:#222}
.t-card small{display:block;margin-top:8px;font-size:14px}
.qmark{position:absolute;right:24px;bottom:-26px;font:700 80px/1 'Poppins',sans-serif;color:var(--copper)}
.chev{position:absolute;top:347px}

/* contact */
.contact{top:2779px;height:594px}
.contact .sec-title{margin-top:84px}
.contact-photo{position:absolute;left:111px;top:178px;width:316px;height:317px;background:linear-gradient(160deg,#c9c6c1,#9c9893 60%,#6f6b67)}
.contact-block{position:absolute;left:93px;top:400px;width:100px;height:116px;background:var(--navy)}
.field{position:absolute;border:1px solid #8a909a;border-radius:5px;font:400 14px 'Roboto',sans-serif;color:#555;padding:19px 26px}
.field span{color:var(--copper)}
.submit{position:absolute;left:463px;top:458px;width:161px;height:40px}

/* footer */
.footer{top:3373px;height:434px;background:linear-gradient(180deg,#4a5568,#3b4556);color:var(--white)}
.f-brand{position:absolute;left:111px;top:240px;width:272px;text-align:center;font:500 52px/1 'Poppins',sans-serif;letter-spacing:1px}
.f-brand small{display:block;font:400 20px 'Poppins',sans-serif;letter-spacing:5px;margin-top:6px}
.f-brand .sq{width:60px;height:60px;border:5px solid var(--white);margin:0 auto 22px}
.f-col{position:absolute;top:80px}
.f-col h5{font:500 25px 'Roboto',sans-serif}
.f-col .line{width:44px;height:3px;background:var(--white);margin:12px 0 20px}
.f-col li{list-style:none;font:500 16.5px 'Roboto',sans-serif;margin-bottom:16px;display:flex;align-items:center;gap:14px}
.f-col li i{width:8px;height:8px;border-top:2px solid var(--copper);border-right:2px solid var(--copper);transform:rotate(45deg)}
.f-col.c2 li{margin-bottom:50px;gap:16px}
.f-col.c2 li i{width:13px;height:13px;border:0;border-radius:50%;background:var(--copper);transform:none}
.f-base{position:absolute;left:111px;right:111px;top:352px;border-top:1px solid rgba(255,255,255,.3)}
.copy{position:absolute;top:380px;width:100%;text-align:center;font:400 16px 'Roboto',sans-serif}
.code{position:absolute;right:43px;top:383px;font-size:13px}
</style>
</head>
<body>

<header class="hero">
  <div class="abs" role="img" aria-label="Photo of a hand handing over house keys above an open palm, with a small house model and tablet on a table" style="inset:0"></div>
  <div class="abs topbar" style="left:0;width:1200px">
    <div class="item" style="left:111px"><i class="ic"></i>555-014-2290</div>
    <div class="item" style="left:284px"><i class="ic"></i>info@meridianescrow.com</div>
    <div class="social"><i></i><i></i><i></i></div>
  </div>
  <div class="brand"><div class="sq"></div><div>MERIDIAN<small>ESCROW PARTNERS</small></div></div>
  <nav class="nav"><span class="active">Home</span><span>About Us</span><span>Services</span><span>Contact Us</span></nav>
  <a class="btn quote">Get a Quote</a>
  <h1>Escrow<br>Accounting<br>Services</h1>
  <a class="btn get-started">Get Started</a>
  <div class="arrows">
    <span><svg width="12" height="14" viewBox="0 0 12 14"><path d="M8 2 3 7l5 5" fill="none" stroke="#333" stroke-width="2"/></svg></span>
    <span><svg width="12" height="14" viewBox="0 0 12 14"><path d="M4 2l5 5-5 5" fill="none" stroke="#333" stroke-width="2"/></svg></span>
  </div>
</header>

<section class="about">
  <div class="about-photo" role="img" aria-label="Photo of an accountant typing on a laptop beside a calculator and notebook"></div>
  <div class="about-box"></div>
  <h2>About <span>Us</span></h2>
  <div class="rule"></div>
  <p>Meridian Escrow Partners has accounting experts who understand the title industry and the importance of compliance, security, and implementing precise escrow accounting procedures along with timely monthly reporting.</p>
  <a class="btn learn">Learn More<i class="dot"></i></a>
  <div class="dots" style="left:135px;top:286px;width:22px;height:70px"></div>
  <div class="dots" style="left:135px;top:345px;width:84px;height:22px"></div>
</section>

<section class="band">
  <h3>Our team of experienced professionals is</h3>
  <h4>The ideal solution for your needs.</h4>
  <div class="btns">
    <a class="btn dark">Our Services<i class="dot"></i></a>
    <a class="btn light">Get in Touch<i class="dot"></i></a>
  </div>
</section>

<section class="services">
  <h2 class="sec-title">Our <span>Services</span></h2>
  <div class="rule"></div>
  <div class="card tl">
    <svg width="56" height="58" viewBox="0 0 56 58" fill="none" stroke="#fff" stroke-width="2"><path d="M28 56V30L10 12M28 30 46 12M4 6h12v12M52 6H40v12"/></svg>
    Daily two-way reconciliation is a Best Practice Standard. Let us create a customized package that ensures your compliance and protects your reporting from audit deficiencies.
  </div>
  <div class="card tr">
    <svg width="46" height="50" viewBox="0 0 46 50" fill="none" stroke="#fff" stroke-width="2"><path d="M2 48h42M6 48V36h8v12M18 48V28h8v20M30 48V20h8v28M6 26 36 6M28 6h8v8"/></svg>
    Comprehensive daily and monthly reports will be delivered securely using VaultLink. These reports will include a detailed breakdown of items that may require your attention. We also manage the submission of reconciliations to underwriters.
  </div>
  <div class="card bl">
    <svg width="54" height="52" viewBox="0 0 54 52" fill="none" stroke="#fff" stroke-width="2"><rect x="2" y="2" width="50" height="36"/><path d="M2 10h50M20 50h14M27 38v12M22 20l-5 5 5 5M32 20l5 5-5 5M29 18l-4 14"/></svg>
    We perform reconciliations across all accounting software systems using secure protocols aligning with NTIA Best Practice - Pillar 3 standards.
  </div>
  <div class="card br">
    <svg width="54" height="54" viewBox="0 0 54 54" fill="none" stroke="#fff" stroke-width="2"><path d="M2 40c8-6 16-6 22-2h10c3 0 3 4 0 4H22M2 50l10-4 14 4 24-14c2-2 0-5-3-4L34 40"/><circle cx="32" cy="22" r="9"/><path d="M40 6h12v20H40M14 4v18M10 8l4-4 4 4"/></svg>
    Our affordable rates allow your company to significantly enhance efficiency with minimal investment and focus on what matters. Pricing is based on account activity volume, and we offer discounts for multiple accounts.
  </div>
  <div class="hub"><i></i></div>
</section>

<section class="clients">
  <h2 class="sec-title">See what <span>our clients think</span></h2>
  <div class="rule"></div>
  <svg class="chev" style="left:48px" width="12" height="20" viewBox="0 0 12 20"><path d="M10 2 2 10l8 8" fill="none" stroke="#333" stroke-width="2"/></svg>
  <svg class="chev" style="left:1138px" width="12" height="20" viewBox="0 0 12 20"><path d="M2 2l8 8-8 8" fill="none" stroke="#333" stroke-width="2"/></svg>
  <div class="t-card" style="left:111px">
    <div class="stars">★★★★★</div>
    <q>Lorem ipsum dolor sit amet, conse ctetur adipiscing elit, sed do eiusmod tempor incididunt ut labore et dolore magna aliqua. Ut enim ad minim veniam, quis nostrud exercitation commodo consequat.</q>
    <hr><b>John Doe</b><small>Company name</small>
  </div>
  <div class="t-card feat" style="left:445px">
    <div class="stars">★★★★★</div>
    <q>Lorem ipsum dolor sit amet, conse ctetur adipiscing elit, sed do eiusmod tempor incididunt ut labore et dolore magna aliqua. Ut enim ad minim veniam, quis nostrud exercitation commodo consequat.</q>
    <hr><b>John Doe</b><small>Company name</small>
    <div class="qmark">“</div>
  </div>
  <div class="t-card" style="left:782px">
    <div class="stars">★★★★★</div>
    <q>Lorem ipsum dolor sit amet, conse ctetur adipiscing elit, sed do eiusmod tempor incididunt ut labore et dolore magna aliqua. Ut enim ad minim veniam, quis nostrud exercitation commodo consequat.</q>
    <hr><b>John Doe</b><small>Company name</small>
  </div>
</section>

<section class="contact">
  <h2 class="sec-title">Get in <span>Touch</span></h2>
  <div class="rule"></div>
  <div class="dots" style="left:85px;top:152px;width:86px;height:22px"></div>
  <div class="dots" style="left:85px;top:152px;width:22px;height:88px"></div>
  <div class="contact-block"></div>
  <div class="contact-photo" role="img" aria-label="Portrait photo of the company founder in a light jacket"></div>
  <div class="field" style="left:463px;top:178px;width:304px;height:53px">Name <span>*</span></div>
  <div class="field" style="left:784px;top:178px;width:305px;height:53px">Email address <span>*</span></div>
  <div class="field" style="left:463px;top:249px;width:626px;height:53px">Phone <span>*</span></div>
  <div class="field" style="left:463px;top:320px;width:626px;height:122px">Message</div>
  <a class="btn submit">Submit Now</a>
</section>

<footer class="footer">
  <div class="f-brand"><div class="sq"></div>MERIDIAN<small>ESCROW PARTNERS</small></div>
  <div class="f-col" style="left:547px">
    <h5>Quick Links</h5><div class="line"></div>
    <ul><li><i></i>Home</li><li><i></i>About Us</li><li><i></i>Services</li><li><i></i>Contact Us</li><li><i></i>Privacy Policy</li></ul>
  </div>
  <div class="f-col c2" style="left:795px">
    <h5>Contact Us</h5><div class="line"></div>
    <ul style="margin-top:26px"><li><i></i>www.meridianescrowpartners.com</li><li><i></i>jcarter@meridianescrow.com</li><li><i></i>555-014-2290</li></ul>
  </div>
  <div class="f-base"></div>
  <div class="copy">© Copyrights 2024 | All Rights Reserved</div>
  <div class="code">C38</div>
</footer>

</body>
</html>
```